Need a business card for a Construction and Remodeling company.
Our company logo is the fleur de lis design as thats the family crust that we use on our logos.
Heres the info it needs:

Brackmore Construction & Remodeling, LLC
Renovations * Restorations

Elwin R. Brackmore
845 North Quarry Road
Larkfield Harbor 04821
(203) 555.0182
CT LIC/REG: 418257

home owners, customers

```html
<!DOCTYPE html>
<html lang="en">
<head>
<meta charset="utf-8">
<title>Brackmore Construction &amp; Remodeling — Business Card</title>
<link rel="stylesheet" href="https://fonts.googleapis.com/css2?family=Cinzel:wght@400;600&family=Open+Sans:wght@400&display=swap">
<style>
  :root {
    --backdrop: #1f1f20;
    --card-black: #121212;
    --card-white: #ffffff;
    --gold: #c0902e;
    --ink: #1a1a1a;
    --ink-soft: #3a3a3a;
    --silver: #e9e9e9;
  }
  * { box-sizing: border-box; margin: 0; padding: 0; }
  html, body {
    width: 1200px; height: 900px; overflow: hidden;
    background: var(--backdrop);
  }
  .canvas {
    position: relative; width: 1200px; height: 900px;
    display: flex; flex-direction: column; align-items: center; justify-content: center; gap: 40px;
  }
  .card {
    position: relative; width: 660px; height: 377px;
    box-shadow: 0 10px 30px rgba(0,0,0,.45);
  }
  .card--front { background: var(--card-black); }
  .card--back { background: var(--card-white); }

  .brand { position: absolute; text-align: center; font-family: "Cinzel", serif; }
  .brand__dot {
    display: block; width: 38px; height: 38px; border-radius: 50%;
    background: var(--gold); margin: 0 auto 18px;
  }
  .brand__name { display: block; font-size: 46px; letter-spacing: 4px; line-height: 1; font-weight: 400; }
  .brand__legal { display: block; font-size: 11.5px; letter-spacing: 1px; margin-top: 6px; font-weight: 400; }

  .card--front .brand { left: 0; right: 0; top: 74px; color: var(--silver); }
  .services {
    position: absolute; left: 0; right: 0; top: 256px; text-align: center;
    font-family: "Cinzel", serif; color: var(--gold); font-size: 14px; letter-spacing: 1.5px;
  }
  .services__sep { margin: 0 16px; }

  .card--back .brand { right: 40px; top: 118px; width: 300px; color: var(--ink); }
  .card--back .brand__name { font-size: 40px; }

  .holder { position: absolute; left: 54px; top: 58px; }
  .holder__name { font-family: "Cinzel", serif; font-size: 24px; font-weight: 400; letter-spacing: 1px; color: var(--ink); }
  .holder__license { font-family: "Open Sans", sans-serif; font-size: 13px; color: var(--gold); margin-top: 0; }

  .contact { position: absolute; left: 54px; top: 208px; list-style: none;
    font-family: "Open Sans", sans-serif; font-size: 15px; color: var(--ink-soft); }
  .contact__item { display: flex; align-items: center; gap: 9px; line-height: 25px; }
  .contact__icon { width: 14px; height: 14px; fill: var(--gold); flex: none; }
  .contact__spacer { width: 14px; flex: none; }
</style>
</head>
<body>
<main class="canvas">
  <section class="card card--front" aria-label="Card front">
    <div class="brand">
      <span class="brand__dot"></span>
      <span class="brand__name">BRACKMORE</span>
      <span class="brand__legal">Construction &amp; Remodeling, LLC</span>
    </div>
    <p class="services">Renovations<span class="services__sep">|</span>Additions<span class="services__sep">|</span>Restorations.</p>
  </section>

  <section class="card card--back" aria-label="Card back">
    <div class="holder">
      <h1 class="holder__name">ELWIN R. BRACKMORE</h1>
      <p class="holder__license">LIC/REG: 418257</p>
    </div>
    <ul class="contact">
      <li class="contact__item">
        <svg class="contact__icon" viewBox="0 0 16 16"><path d="M1 6c0-2 3-3 7-3s7 1 7 3v1h-3.5V5.5h-7V7H1zM4 8h8l2 6H2z"/></svg>
        (203) 555-0182
      </li>
      <li class="contact__item">
        <svg class="contact__icon" viewBox="0 0 16 16"><path d="M1 3h14v10H1zM2 4l6 5 6-5v1L8 10 2 5z" fill-rule="evenodd"/></svg>
        office@brackmorebuild.com
      </li>
      <li class="contact__item">
        <svg class="contact__icon" viewBox="0 0 16 16"><path d="M8 1a5 5 0 0 1 5 5c0 4-5 9-5 9S3 10 3 6a5 5 0 0 1 5-5zm0 3a2 2 0 1 0 0 4 2 2 0 0 0 0-4z" fill-rule="evenodd"/></svg>
        845 North Quarry Road
      </li>
      <li class="contact__item">
        <span class="contact__spacer"></span>
        Larkfield Harbor 04821
      </li>
    </ul>
    <div class="brand">
      <span class="brand__dot"></span>
      <span class="brand__name">BRACKMORE</span>
      <span class="brand__legal">Construction &amp; Remodeling, LLC</span>
    </div>
  </section>
</main>
</body>
</html>
```